VeltaFilez Website

VeltaFiles - Organized Medical Docz
We need a Web design for a new company called - VeltaFilez.
VeltaFilez is a Personal Injury and Medical Record Legal Service Outsourcing company. We help Personal Injury Attorneys - with fact based Medical Chronologies and Summaries.

We take Medical Records in disarray and put them in order and summarize them in a chronological order and Update them as needed (if more medical records are added)
Take Releases (for medical records) and work with doctor practices and get the records if needed

Target Market(s)

Personal Injury Attorneys

Industry/Entity Type

Attorney

Number of Pages Required

2 page

Font styles to use
Serif
Sans Serif

Colors

Designer to choose colors to be used in the design.

Requirements
Must have
• Professional Design
• Just need the design for the Home page and Internal pages - I will do the Coding for the pages in html and/or wordpress.
• Don't worry about the content - just need a design.

```html
<!DOCTYPE html>
<html lang="en">
<head>
<meta charset="utf-8">
<title>VeltaFilez – Home</title>
<link href="https://fonts.googleapis.com/css2?family=Roboto:wght@400;500;700&display=swap" rel="stylesheet">
<style>
:root{
  --blue:#2391ef;
  --blue-dark:#1b3f78;
  --blue-link:#3a78c9;
  --page:#efefef;
  --white:#ffffff;
  --text:#555b63;
  --rule:#e2e2e2;
  --footer:#333333;
  --red:#d92a2a;
  --green:#6bd4ab;
}
*{box-sizing:border-box;margin:0;padding:0}
html,body{width:686px;height:1200px;overflow:hidden}
body{position:relative;background:var(--page);font-family:'Roboto',sans-serif;color:var(--text)}
.abs{position:absolute}

/* header */
.site-header{left:0;top:0;width:686px;height:53px;background:var(--white);display:flex;align-items:center;justify-content:center}
.brand{color:var(--blue-dark);font-weight:500;font-size:16px;letter-spacing:.3px}

/* hero */
.hero{left:0;top:53px;width:686px;height:251px;background:var(--blue)}
.hero-title{left:0;top:36px;width:686px;text-align:center;color:var(--white);font-weight:700;font-size:17.5px;line-height:24px;letter-spacing:.6px}
.hero-art{left:125px;top:83px;width:561px;height:112px;background:linear-gradient(90deg,rgba(255,255,255,.18),rgba(255,255,255,.28),rgba(255,255,255,.18));border-radius:4px}

/* cards */
.card{background:var(--white);box-shadow:0 1px 4px rgba(0,0,0,.25)}
.welcome{left:48px;top:249px;width:589px;height:131px;text-align:center;padding:26px 32px 0}
.section-title{color:var(--blue-dark);font-weight:700;font-size:16px;letter-spacing:.8px}
.body-text{font-size:7.6px;line-height:12px;letter-spacing:.1px}
.welcome .body-text{margin-top:8px}

.about{left:48px;top:406px;width:589px;height:171px}
.about .section-title{position:absolute;left:29px;top:15px}
.about-text{left:29px;top:47px;width:340px}
.about-text p+p{margin-top:12px}
.about-art{left:404px;top:16px;width:169px;height:136px;background:var(--green);box-shadow:0 1px 3px rgba(0,0,0,.3)}

.services-band{left:0;top:606px;width:686px;height:108px;background:var(--blue)}
.services-band h2{margin-top:19px;text-align:center;color:var(--white);font-size:17px;font-weight:500;letter-spacing:.5px}
.services{left:48px;top:665px;width:589px;height:424px}
.service{position:absolute;left:0;width:589px;height:106px;border-bottom:1px solid var(--rule)}
.service:last-child{border-bottom:none}
.service::before{content:"";position:absolute;left:121px;top:10px;width:1px;height:86px;background:var(--rule)}
.service h3{position:absolute;left:135px;top:18px;color:var(--blue-link);font-size:9.6px;font-weight:700;letter-spacing:.5px}
.service .body-text{position:absolute;left:135px;top:39px;width:420px}
.read-more{position:absolute;right:51px;top:76px;color:var(--blue-link);font-size:7.6px;font-weight:700;text-decoration:underline}

/* contact */
.contact{left:397px;top:896px;width:268px;height:211px;background:var(--white);box-shadow:0 1px 5px rgba(0,0,0,.25)}
.contact-head{height:31px;background:var(--blue);color:var(--white);text-align:center;font-size:10px;font-weight:500;letter-spacing:.6px;line-height:31px}
.field{position:absolute;border-bottom:1px solid #cfcfcf;font-size:7.4px;color:#8a8a8a}
.field .tiny{font-size:4.5px;display:block}
.send{left:101px;top:174px;width:67px;height:19px;background:var(--blue);border-radius:4px;color:var(--white);font-size:8px;font-weight:500;text-align:center;line-height:19px}

.load-more{left:299px;top:1118px;width:88px;height:21px;background:var(--blue);border-radius:4px;color:var(--white);font-size:10px;font-weight:700;text-align:center;line-height:21px}
.fab{left:641px;top:1109px;width:42px;height:42px;border-radius:50%;background:var(--red);box-shadow:0 2px 5px rgba(0,0,0,.35);display:flex;align-items:center;justify-content:center}

.site-footer{left:0;top:1168px;width:686px;height:32px;background:var(--footer);color:var(--white);font-size:6.6px;text-align:center;line-height:32px}

/* sidebar */
.sidebar{left:0;top:0;width:125px;height:1200px;background:var(--white);box-shadow:2px 0 4px rgba(0,0,0,.35)}
.sidebar-head{position:relative;height:94px;background:linear-gradient(135deg,#1d5566 0%,#23687a 55%,#7f6a4f 62%,#255f70 70%,#1f5868 100%);text-align:center}
.sidebar-brand{padding-top:55px;color:var(--white);font-size:10px;font-weight:500;letter-spacing:.4px}
.close-btn{position:absolute;left:104px;top:3px}
.menu{list-style:none;margin-top:22px}
.menu li{height:20px;margin-bottom:12.6px;display:flex;align-items:center;padding-left:9px;font-size:8.4px;color:var(--blue-link)}
.menu li svg{margin-right:7px}
.menu li.active{background:#ededed;border-radius:0 6px 6px 0;width:122px;margin-bottom:12px}
</style>
</head>
<body>

<header class="abs site-header">
  <div class="brand">VeltaFilez</div>
</header>

<section class="abs hero">
  <h1 class="abs hero-title">LOREM IPSUM IS SIMPLY DUMMY TEXT OF THE<br>PRINTING AND TYPESETTING</h1>
  <div class="abs hero-art" role="img" aria-label="Row of medical illustrations: flasks, first-aid kits, IV bags, pill packs, hearts and a laptop with a heartbeat line"></div>
</section>

<section class="abs card welcome">
  <h2 class="section-title">WELCOME</h2>
  <p class="body-text">Lorem Ipsum is simply dummy text of the printing and typesetting industry. Lorem Ipsum has been the industry's standard dummy text ever since the 1500s, when an unknown printer took a galley of type and scrambled it to make. Lorem Ipsum is simply dummy text of the printing and typesetting industry. Lorem Ipsum has been the industry's standard dummy text ever since the 1500s, whe. Lorem Ipsum is simply dummy text of the printing and typesetting industry. Lorem Ipsum has been the industry's standard .</p>
</section>

<section class="abs card about">
  <h2 class="section-title">ABOUT US</h2>
  <div class="abs about-text body-text">
    <p>Lorem Ipsum is simply dummy text of the printing and typesetting industry. Lorem Ipsum has been the industry's standard dummy text ever since the 1500s, when an unknown printer took a galley of type and scrambled it to make. Lorem Ipsum is simply dummy text of the printing and typesetting industry. Lorem Ipsum has been the industry's standard dummy text ever since the 1500s, when an unknown printer took a galley of type and scrambled it to make.</p>
    <p>Lorem Ipsum is simply dummy text of the printing and typesetting industry. Lorem Ipsum has been the industry's standard dummy text ever since the 1500s, when an unknown printer took a galley of type and scrambled it to make. 1500.</p>
  </div>
  <div class="abs about-art" role="img" aria-label="Illustration of a doctor surrounded by medical instruments on a mint green background"></div>
</section>

<section class="abs services-band"><h2>OUR SERVICES</h2></section>

<section class="abs card services">
  <article class="service" style="top:0">
    <h3>LOREM IPSUM IS SIMPLY DUMMY</h3>
    <p class="body-text">Lorem Ipsum is simply dummy text of the printing and typesetting industry. Lorem Ipsum has been the industry's standard dummy text ever since the 1500s, when an unknown printer took a galley of type and scrambled it to make.</p>
    <span class="read-more">Read More</span>
  </article>
  <article class="service" style="top:106px">
    <h3>LOREM IPSUM IS SIMPLY DUMMY</h3>
    <p class="body-text">Lorem Ipsum is simply dummy text of the printing and typesetting industry. Lorem Ipsum has been the industry's standard dummy text ever since the 1500s, when an unknown printer took a galley of type and scrambled it to make.</p>
    <span class="read-more">Read More</span>
  </article>
  <article class="service" style="top:212px">
    <h3>LOREM IPSUM IS SIMPLY DUMMY</h3>
    <p class="body-text">Lorem Ipsum is simply dummy text of the printing and typesetting industry. Lorem Ipsum has been the industry's standard dummy text ever since the 1500s, when an unknown printer took a galley of type and scrambled it to make.</p>
  </article>
  <article class="service" style="top:318px">
    <h3>LOREM IPSUM IS SIMPLY DUMMY</h3>
    <p class="body-text">Lorem Ipsum is simply dummy text of the printing and typesetting industry. Lorem Ipsum has been the industry's standard dummy text ever since the 1500s, when an unknown printer took a galley of type and scrambled it to make.</p>
  </article>
</section>

<div class="abs load-more">Load More</div>

<aside class="abs contact">
  <div class="contact-head">CONTACT US</div>
  <div class="field" style="left:13px;top:42px;width:116px;height:16px"><span class="tiny">Name *</span>|</div>
  <div class="field" style="left:138px;top:50px;width:116px;height:8px;line-height:7px">Last Name</div>
  <div class="field" style="left:13px;top:75px;width:241px;height:10px;line-height:8px">Email</div>
  <div class="field" style="left:13px;top:101px;width:241px;height:58px;line-height:8px">Message</div>
  <div class="abs send">Send</div>
</aside>

<div class="abs fab">
  <svg width="16" height="16" viewBox="0 0 16 16" fill="none" stroke="#fff" stroke-width="1.3"><path d="M3 13l1-3.5 7.5-7.5 2.5 2.5L6.5 12z"/><path d="M10 3.5l2.5 2.5"/></svg>
</div>

<footer class="abs site-footer">Copyright © veltafilez | All Rights Reaserved</footer>

<nav class="abs sidebar">
  <div class="sidebar-head">
    <svg class="close-btn" width="16" height="16" viewBox="0 0 16 16" fill="none" stroke="#fff" stroke-width="1.2"><circle cx="8" cy="8" r="6.8"/><path d="M5.3 5.3l5.4 5.4M10.7 5.3l-5.4 5.4"/></svg>
    <div class="sidebar-brand">VeltaFilez</div>
  </div>
  <ul class="menu">
    <li class="active"><svg width="9" height="8" viewBox="0 0 9 8" fill="#3a78c9"><path d="M4.5 0L0 4h1.2v4h2.4V5.5h1.8V8h2.4V4H9z"/></svg>Home</li>
    <li><svg width="9" height="8" viewBox="0 0 9 8" fill="#3a78c9"><path d="M0 0h1v7h8v1H0z"/><rect x="2" y="3" width="1.3" height="3.5"/><rect x="4" y="1" width="1.3" height="5.5"/><rect x="6" y="2.5" width="1.3" height="4"/></svg>Menu 1</li>
    <li><svg width="9" height="8" viewBox="0 0 9 8" fill="#3a78c9"><circle cx="4.5" cy="2" r="2"/><path d="M1 8c0-2.5 1.5-3.5 3.5-3.5S8 5.5 8 8z"/></svg>Menu 2</li>
    <li><svg width="9" height="8" viewBox="0 0 9 8" fill="none" stroke="#3a78c9" stroke-width=".9"><rect x=".5" y="1.5" width="6" height="6"/><path d="M3.5 5l.5-1.5L7.5.5l1 1L5 4.5z" fill="#3a78c9"/></svg>Menu 3</li>
    <li><svg width="9" height="8" viewBox="0 0 9 8" fill="none" stroke="#3a78c9" stroke-width=".9"><path d="M.5.5h6l2 2v5h-8z"/><rect x="2" y=".5" width="4" height="2.5"/><rect x="2" y="4.5" width="5" height="3"/></svg>Menu 4</li>
    <li><svg width="9" height="8" viewBox="0 0 9 8" fill="#3a78c9"><rect x="1.5" y="3.5" width="6" height="4.5"/><path d="M2.8 3.5V2.3a1.7 1.7 0 013.4 0v1.2" fill="none" stroke="#3a78c9" stroke-width=".9"/></svg>Menu 5</li>
  </ul>
</nav>

</body>
</html>
```